The quiet river under A pale orchard in Wintertime: Author/ Writer. Education foriegn language Art.*

Am in need of a book cover, which describes basic alphabets and the fundamentals of a language. Which depicts geometric symbols and Black male/female American image. Collars: At top, light blue with small American flag and stars. With the title in white : The quiet river under A pale orchard in Wintertime. And at bottom, navy blue. With the sub title also in white. Saying Morvadel Quintor. Also this is where the image of the black male and female face neck and shoulders are should show. Under that, it should say! A educational work book. Then Authors pen name: O lune E drav O lune Ko. My budget for this project is $ 200 to 250. This will be an ebook with Brindle and all industry standers pixels. Epub, mobi,pdf. Thank you.

```html
<!DOCTYPE html>
<html lang="en">
<head>
<meta charset="utf-8">
<title>Morvadel Quintor – An educational work book</title>
<link rel="stylesheet" href="https://fonts.googleapis.com/css2?family=Fira+Sans+Condensed:wght@500;600&family=Poppins:wght@700&family=Questrial&display=swap">
<style>
  :root {
    --sky: #1fc4ec;
    --teal: #2fb6b0;
    --magenta: #b8326a;
    --orange: #e8772a;
    --navy: #22305a;
    --denim: #8fa6d6;
    --white: #ffffff;
    --title-shade: #c3c9da;
    --flag-red: #d8232a;
    --flag-blue: #22306b;
  }
  html, body { margin: 0; padding: 0; overflow: hidden; background: #ffffff; }
  .cover {
    position: relative;
    width: 852px;
    height: 1200px;
    overflow: hidden;
  }
  .cover-art {
    position: absolute; inset: 0;
    background:
      radial-gradient(ellipse 60% 35% at 50% 10%, #35d6f5 0%, transparent 70%),
      radial-gradient(circle at 12% 50%, #e05a2e 0%, transparent 30%),
      radial-gradient(circle at 88% 45%, #f0a830 0%, transparent 28%),
      radial-gradient(circle at 45% 40%, #c8306a 0%, transparent 25%),
      radial-gradient(circle at 10% 80%, #2aa06a 0%, transparent 30%),
      linear-gradient(180deg, var(--sky) 0%, var(--teal) 30%, var(--magenta) 60%, var(--orange) 100%);
  }
  .cover-photo {
    position: absolute;
    left: 30px; top: 280px;
    width: 790px; height: 920px;
    border-radius: 200px 200px 0 0;
    background:
      linear-gradient(90deg, var(--denim) 0%, #a9bbe0 40%, var(--navy) 55%, #1c2748 100%);
    opacity: 0.9;
  }
  .flag { position: absolute; left: 350px; top: 40px; width: 152px; height: 85px; }
  .tagline {
    position: absolute; left: 0; right: 0; top: 132px;
    margin: 0;
    text-align: center;
    font-family: "Fira Sans Condensed", sans-serif;
    font-weight: 500;
    font-size: 42px;
    line-height: 56px;
    color: var(--white);
    text-shadow: 0 2px 4px rgba(0,0,0,0.35);
  }
  .tagline .small { font-size: 24px; }
  .book-title {
    position: absolute; left: 0; right: 0; top: 495px;
    margin: 0;
    text-align: center;
    font-family: "Poppins", sans-serif;
    font-weight: 700;
    letter-spacing: -2px;
    text-transform: uppercase;
    background: linear-gradient(180deg, var(--white) 55%, var(--title-shade) 100%);
    -webkit-background-clip: text;
    background-clip: text;
    color: transparent;
    filter: drop-shadow(0 3px 4px rgba(0,0,0,0.45));
  }
  .book-title .line-one { display: block; font-size: 92px; line-height: 110px; }
  .book-title .line-two { display: block; font-size: 104px; line-height: 124px; }
  .subtitle {
    position: absolute; left: 0; right: 0; top: 752px;
    margin: 0;
    text-align: center;
    font-family: "Questrial", sans-serif;
    font-size: 42px;
    color: var(--white);
    text-shadow: 0 2px 4px rgba(0,0,0,0.35);
  }
  .author {
    position: absolute; left: 0; right: 0; top: 1000px;
    margin: 0;
    text-align: center;
    font-family: "Fira Sans Condensed", sans-serif;
    font-weight: 500;
    font-size: 64px;
    color: var(--white);
    text-shadow: 0 2px 5px rgba(0,0,0,0.4);
  }
</style>
</head>
<body>
<main class="cover">
  <div class="cover-art" role="img" aria-label="Colourful psychedelic mandala and flower illustration in blue, teal, magenta and orange"></div>
  <div class="cover-photo" role="img" aria-label="Photograph of a smiling young Black woman and man walking together"></div>

  <svg class="flag" viewBox="0 0 152 85" aria-label="Flag of the United States" role="img">
    <rect width="152" height="85" fill="var(--white)"/>
    <g fill="var(--flag-red)">
      <rect y="0" width="152" height="6.5"/>
      <rect y="13" width="152" height="6.5"/>
      <rect y="26" width="152" height="6.5"/>
      <rect y="39" width="152" height="6.5"/>
      <rect y="52" width="152" height="6.5"/>
      <rect y="65" width="152" height="6.5"/>
      <rect y="78" width="152" height="7"/>
    </g>
    <rect width="65" height="45.5" fill="var(--flag-blue)"/>
    <g fill="var(--white)">
      <circle cx="8" cy="6" r="1.5"/><circle cx="19" cy="6" r="1.5"/><circle cx="30" cy="6" r="1.5"/><circle cx="41" cy="6" r="1.5"/><circle cx="52" cy="6" r="1.5"/>
      <circle cx="13" cy="15" r="1.5"/><circle cx="24" cy="15" r="1.5"/><circle cx="35" cy="15" r="1.5"/><circle cx="46" cy="15" r="1.5"/><circle cx="57" cy="15" r="1.5"/>
      <circle cx="8" cy="24" r="1.5"/><circle cx="19" cy="24" r="1.5"/><circle cx="30" cy="24" r="1.5"/><circle cx="41" cy="24" r="1.5"/><circle cx="52" cy="24" r="1.5"/>
      <circle cx="13" cy="33" r="1.5"/><circle cx="24" cy="33" r="1.5"/><circle cx="35" cy="33" r="1.5"/><circle cx="46" cy="33" r="1.5"/><circle cx="57" cy="33" r="1.5"/>
      <circle cx="8" cy="41" r="1.5"/><circle cx="19" cy="41" r="1.5"/><circle cx="30" cy="41" r="1.5"/><circle cx="41" cy="41" r="1.5"/><circle cx="52" cy="41" r="1.5"/>
    </g>
  </svg>

  <p class="tagline">The quiet river <span class="small">under</span> A pale orchard<br><span class="small">in</span> Wintertime</p>

  <h1 class="book-title"><span class="line-one">Morvadel</span><span class="line-two">Quintor</span></h1>

  <p class="subtitle">An educational work book</p>

  <p class="author">O lune E drav O lune Ko</p>
</main>
</body>
</html>
```